Indonesian B2B Company (Varo Ingredients) - Stationery Design

Varo Ingredients needs a corporate, bold and professional-looking stationery design.

Varo Ingredients is a new Indonesian company manufacturing, marketing and distributing various ingredients / raw materials such as flavours, fragrance, colours, sweeteners, preservatives for the food & beverage, pharmaceutical, personal care and other household goods industries.

It is a business to business (B2B) company as we supply various natural and synthetic raw materials to various consumer goods manufacturers. We therefore need a logo/identity with corporate and industrial style.

Varo Ingredients is a startup company which belongs to a larger Tumina Jaya group of companies (http://tuminajaya.bizplank.example/about) that focuses in the mining, petroleum and energy businesses. Varo Ingredients would like to focus in providing good quality, safe, reliable and affordable ingredients for the industries. Our tagline is "Ingredients for Your Success"
Updates

We have updated some information including our requirements and contact details to be shown in the stationery. Please check the project brief.

Regards,

Varo Ingredients

Target Market(s)

Manufacturers of food & beverages, personal care, pharmaceutical and other FMCG factories.

Industry/Entity Type

Business

Requirements
Must have
• Smart, professional and corporate touches in the stationery designs. We require designs for:
1. Letterhead
2. Envelope (with and without window)
3. Name card
4. Powerpoint presentation template
5. CD label
6. Small memo / with compliments card

Contact details:

Company name:
PT Varo Ingredients

Address:
Ruko Pelita Sumber Asri, Blok K07 no: 15-16
Cempaka Hijau Utara, 14590
Indonesia

Tel:+62 21 738 2096
Fax:+62 21 738 2097
Email: info@varo-ingredients.example
Website: www.varo-ingredients.example

```html
<!DOCTYPE html>
<html lang="en">
<head>
<meta charset="utf-8">
<title>Varo Ingredients – Name Card</title>
<link href="https://fonts.googleapis.com/css2?family=Barlow:wght@500;600&family=Source+Sans+3:wght@400;600&display=swap" rel="stylesheet">
<style>
  :root {
    --brand-red: #c1272d;
    --accent-red: #d1232f;
    --tint-red: #e0555a;
    --ink: #3d3d3d;
    --muted: #8a8a8a;
    --soft-grey: #e4e4e4;
    --paper: #ffffff;
    --backdrop: #2b2b2b;
  }
  * { box-sizing: border-box; margin: 0; padding: 0; }
  html, body {
    width: 1200px;
    height: 533px;
    overflow: hidden;
    background: var(--backdrop);
  }
  .stage {
    position: relative;
    width: 1200px;
    height: 533px;
  }
  .card {
    position: absolute;
    top: 134px;
    width: 467px;
    height: 266px;
    overflow: hidden;
  }
  .card--front {
    left: 119px;
    background: var(--paper);
  }
  .card--back {
    left: 614px;
    background: var(--brand-red);
  }

  /* Shared decoration spanning the card pair */
  .card-decoration {
    position: absolute;
    top: 12px;
    width: 243px;
    height: 243px;
    border-radius: 50%;
  }
  .card--front .card-decoration {
    left: 291px;
    background: radial-gradient(circle at 40% 50%, #f3f3f3 0%, var(--soft-grey) 100%);
  }
  .card--back .card-decoration {
    left: -63px;
    background: radial-gradient(circle at 60% 50%, var(--tint-red) 0%, #d23a40 100%);
  }

  /* Front */
  .brand-mark {
    position: absolute;
    left: 52px;
    top: 30px;
    width: 44px;
    height: 44px;
    background: var(--brand-red);
  }
  .brand-name {
    position: absolute;
    left: 18px;
    top: 96px;
    font-family: "Barlow", sans-serif;
    font-weight: 500;
    font-size: 21px;
    color: var(--brand-red);
    letter-spacing: -0.2px;
  }
  .brand-tagline {
    position: absolute;
    left: 25px;
    top: 122px;
    font-family: "Barlow", sans-serif;
    font-weight: 500;
    font-size: 10.5px;
    color: var(--muted);
  }
  .company {
    position: absolute;
    left: 18px;
    top: 150px;
    font-family: "Source Sans 3", sans-serif;
    font-style: normal;
    font-size: 13px;
    line-height: 17px;
    color: var(--ink);
  }
  .company__name {
    font-weight: 600;
    color: var(--accent-red);
  }
  .contacts {
    position: absolute;
    left: 18px;
    top: 214px;
    display: grid;
    grid-template-columns: 12px 116px 16px auto;
    row-gap: 1px;
    font-family: "Source Sans 3", sans-serif;
    font-size: 13px;
    line-height: 16px;
    color: var(--ink);
  }
  .contacts__label {
    font-weight: 600;
    color: var(--accent-red);
  }

  /* Back */
  .back-name {
    position: absolute;
    left: 218px;
    top: 105px;
    font-family: "Barlow", sans-serif;
    font-weight: 500;
    font-size: 30px;
    color: var(--paper);
    letter-spacing: -0.3px;
  }
  .back-tagline {
    position: absolute;
    left: 227px;
    top: 143px;
    font-family: "Barlow", sans-serif;
    font-weight: 600;
    font-size: 15px;
    color: var(--paper);
  }
</style>
</head>
<body>
<main class="stage">
  <section class="card card--front" aria-label="Name card, front">
    <div class="card-decoration" role="img" aria-label="Large brand graphic running across to the back of the card"></div>
    <div class="brand-mark" aria-hidden="true"></div>
    <p class="brand-name">Varo Ingredients</p>
    <p class="brand-tagline">Ingredients for Your Success</p>
    <address class="company">
      <span class="company__name">PT Varo Ingredients</span><br>
      Ruko Pelita Sumber Asri, Blok K07 No: 15-16<br>
      Cempaka Hijau Utara, 14590, Indonesia
    </address>
    <div class="contacts">
      <span class="contacts__label">T</span><span>+62 21 738 2096</span>
      <span class="contacts__label">E</span><span>info@varo-ingredients.example</span>
      <span class="contacts__label">F</span><span>+62 21 738 2097</span>
      <span class="contacts__label">W</span><span>www.varo-ingredients.example</span>
    </div>
  </section>

  <section class="card card--back" aria-label="Name card, back">
    <div class="card-decoration" role="img" aria-label="Large brand graphic continuing from the front of the card"></div>
    <p class="back-name">Varo Ingredients</p>
    <p class="back-tagline">Ingredients for Your Success</p>
  </section>
</main>
</body>
</html>
```